B.K. Pronto Shop

The design is for eCommerce home page but I would like it to complement this site: http://www.bkprontosystems.com/ but... it should also have independence as a standalone site.

The best design will be able to effectively mix corporate with a high quality small business consumer feel. It should be completely custom design, not a template look or feel. I want the users to get the feeling that this is the place to go for buying tech for business. We sell the same products as QXR.

You can be creative as you wish, as long as the elements of a great eCommerce site are present.

I would like your 'design' to blow these away:
http://www.store.vantrel.com/
mirbosa.com
http://www.qxr.com/

Here are references:
Call to action
http://tradewisely.net/us/blog/62829-seven-tips-for-designing-an-effective-ecommerce-call-to-action

Effective Ecommerce design
http://www.bizlume.com/ss/7-tips-for-effective-e-commerce#0

91 points of ecommerce
http://ranqo.com/blog/holygrail-of-ecommerce-conversion-optimization-91-points-checklist

UPDATE 07/11/2013:

Please look at the category sample png files. I see already many people are using the main menu from bkprontosystems.com and I do not mind your creativiety, but this is an eCommerce store and people need a menu to get to the categories and/or product types. I don't want to limit anyone creativity by the png samples. I'm also not using them to show I like them in any particular way or form, just that it's needed, whether it's a button (dropdown of course) that says 'Categories' or 'Products, whether it an accordion, horizontal or vertical.

Thanks

UPDATE 07/12/2013:

Please find other use of space that has been used for About Us paragraph (if you've added it to the page). About Us should have it's own page and the purpose of the design should be to sell products (and some services as products). Please put a link or some other creative method to lead users to the About Us page.

Reason: I've raised the award, including 1st, 2nd, and 3rd place and participation payments so I will also extend 7 days. Thanks!

I've updated the product brief. Please scroll down to where it says: UPDATE 07/11/2013

Thanks!

UPDATE 07/12/2013:

Please find other use of space that has been used for About Us paragraph (if you've added it to the page).  About Us should have it's own page and the purpose of the design should be to sell products (and some services as products). Please put a link or some other creative method to lead users to the About Us page if you must but not on the real estate of the page.

Thanks!

Added updates to the brief 7/14/2013.

Thanks!

The voting is in and the project is complete.  Thanks everyone for joining, all of those who participated are truly amazingly talented. But, there were only 3 prizes.  I will be having further projects down the line to develop other pages to this site after the initial implementation is completed.  I truly would like to have you all back. 

- Thank you.

Target Market(s)

corporate decision-makers AND small business consumers

Industry/Entity Type

Small Business

Requirements
Must have
• Call to action.
Openness (non-clutter).

These elements:
Search box
Logo
Tagline
Telephone number
Contact details
Address
My account / sign in
Shopping basket / checkout link
Latest offers
Promotional area
Email sign up
Delivery information
About us
Link to press office / corporate site
Terms and conditions
Sitemap for the footer.
Delivery offers: free
Personalized recommendations
Social media links
Accepted payment methods
Link to blog or community section
Change language / country

http://brightnotes.pellwix.com/sales-leads-landing-page/

UPDATE 07/14/2013
Category Menu. This can be a dropdown, horizontal, vertical, etc. But shoppers need to know how to get to the products they want to buy.
Nice to have
• Trustmarks
Blog/Blog link

UPDATE 07/12/2013:
Make the footer useful.

UPDATE 07/14/2013 (Suggestions of elements to differentiate your designs)

-Quick Shop: A quick buy module/section: Where a user can put in a SKU number or Model number to quickly add the product to their shopping cart.

-Featured
-Best Sellers
-Specials
-Trending Tags/Tag Cloud
- Activity Stream
- Cross Sell/ Up Sell
- Testimonial
- Social Network Feed
- Live Help
- Feedback/Support/Contact Tab
- Show logged in user (i.e. Welcome, Peter Varn)
Should not have
• The design SHOULD NOT be generic like this:

http://www.artflock.com/design/52392
http://www.hollowmart.com/

The page should not feel over cluttered. It should not have low quality icons or design elements. Navigation should not be hard to discover or confusing.

```html
<!DOCTYPE html>
<html lang="en">
<head>
<meta charset="utf-8">
<title>B.K. Pronto Shop – Hardware</title>
<link href="https://fonts.googleapis.com/css2?family=Open+Sans:ital,wght@0,400;0,600;0,700;1,400&display=swap" rel="stylesheet">
<style>
:root{
  --topbar:#3b3b3b;
  --blue:#2a72b0;
  --blue-dark:#1d5a8f;
  --blue-deep:#174b79;
  --blue-text:#24679f;
  --orange:#f28a1e;
  --orange-dark:#e0701a;
  --red:#e9403f;
  --red-dark:#cf2f2e;
  --band:#3f3f3f;
  --card-head:#4a4442;
  --card-foot:#ececec;
  --text:#444;
  --muted:#888;
  --footer:#2c2c2c;
  --footer-bottom:#1b1b1b;
  --page:#f7f7f7;
}
*{box-sizing:border-box;margin:0;padding:0}
html,body{width:1092px;height:1200px;overflow:hidden}
body{font-family:"Open Sans",Arial,sans-serif;color:var(--text);background:var(--page);position:relative;font-size:12px}
.abs{position:absolute}
a{color:inherit;text-decoration:none}

/* top bar */
.topbar{left:0;top:0;width:1092px;height:36px;background:var(--topbar)}
.country{left:114px;top:9px;width:143px;height:20px;background:#f4f4f4;border-radius:2px;font-size:11px;color:#666;display:flex;align-items:center;padding-left:6px;gap:6px}
.country .flag{width:13px;height:9px;background:#2c4f8f;border:1px solid #ccc}
.country .caret{margin-left:auto;width:20px;height:20px;border-left:1px solid #ccc;display:flex;align-items:center;justify-content:center}
.social-top{top:10px;width:16px;height:16px;background:#555;border-radius:3px}
.welcome{left:601px;top:0;width:366px;height:36px;background:linear-gradient(#2f7dbf,#1d5f9a);color:#fff;display:flex;align-items:center;padding:0 18px 0 23px}
.welcome .hello{font-style:italic;font-size:14px}
.welcome .links{margin-left:auto;font-size:11px}

/* header */
.header{left:0;top:36px;width:1092px;height:83px;background:#fff}
.logo{left:115px;top:52px;display:flex;align-items:center;gap:8px}
.logo .mark{width:44px;height:44px;border-radius:50%;background:var(--blue-dark)}
.logo .name{font-size:18px;line-height:19px;font-weight:700;color:var(--blue-dark);letter-spacing:.3px}
.divider{left:287px;top:46px;width:1px;height:60px;background:#ddd}
.tagline{left:307px;top:70px;font-size:13px;color:var(--blue-dark)}
.tagline span{color:#3f96d6}
.help{left:620px;top:46px;width:204px;text-align:right}
.help h2{font-size:19px;font-weight:400;color:var(--blue-dark);line-height:22px}
.help p{font-size:12.5px;color:#555;line-height:17px;margin-right:42px}
.help b{font-weight:700;color:#333}
.phone-btn{left:789px;top:73px;width:35px;height:34px;background:var(--orange);border-radius:3px;display:flex;align-items:center;justify-content:center}
.livehelp{left:837px;top:46px;width:130px;height:61px;background:linear-gradient(#f59a36,var(--orange-dark));border-radius:3px;color:#fff;text-align:center}
.livehelp .t1{font-size:20px;margin-top:7px;line-height:24px}
.livehelp .t2{font-size:12px}

/* nav */
.nav{left:0;top:119px;width:1092px;height:40px;background:linear-gradient(#3a8bcd,#2569a6);border-top:1px solid #5aa4dc}
.nav-item{top:0;height:40px;color:#fff;font-size:14px;display:flex;align-items:center;justify-content:center;gap:9px;border-right:1px solid #1d5a8f}
.nav-item.active{background:var(--blue-deep)}
.caret-w{width:0;height:0;border-left:4px solid transparent;border-right:4px solid transparent;border-top:5px solid #fff}
.cart{left:762px;top:0;width:210px;height:40px;background:var(--blue-deep);color:#fff;display:flex;align-items:center;font-size:14px}
.cart .icon{width:48px;height:40px;display:flex;align-items:center;justify-content:center;border-right:1px solid #2a6aa2}
.cart .sum{margin-left:26px}

/* dark band */
.band{left:0;top:159px;width:1092px;height:161px;background:repeating-linear-gradient(45deg,#3a3a3a 0 2px,#424242 2px 4px)}

/* special offers */
.offers{left:105px;top:170px;width:657px;height:121px;background:#fff}
.offer-tag{left:105px;top:173px;width:108px;height:114px}
.offer-tag .label{position:absolute;left:0;top:32px;width:88px;text-align:center;color:#fff;font-size:16px;line-height:21px}
.offer-arrows{left:111px;top:263px;display:flex;gap:2px}
.offer-arrows span{width:22px;height:21px;background:#fff;display:flex;align-items:center;justify-content:center;color:#333;font-size:13px}
.offer-arrows span:first-child{background:#f26a69;color:#fff}
.offer-strip{left:220px;top:176px;width:542px;height:113px;overflow:hidden}
.mini{position:absolute;top:0;width:105px;height:113px;background:#f3f3f3;border:1px solid #ddd}
.mini .head{height:25px;background:var(--card-head);color:#fff;font-size:12.5px;font-weight:600;padding-left:10px;line-height:25px;white-space:nowrap;overflow:hidden}
.mini .pic{height:58px;margin:6px 22px 0;background:linear-gradient(#fff,#e3e3e3);border:3px solid #2b2b2b;border-radius:2px;width:59px}
.mini .foot{position:absolute;bottom:0;left:0;right:0;height:24px;display:flex;align-items:center;padding:0 6px 0 11px;font-size:12.5px;color:#555;background:#e6e6e6}
.plus{margin-left:auto;width:20px;height:18px;background:#3d3d3d;border-radius:3px;display:flex;align-items:center;justify-content:center}

/* quick shop */
.quick{left:770px;top:173px;width:197px;height:122px;background:linear-gradient(#f04a48,var(--red-dark));color:#fff;padding:6px 10px}
.quick h3{font-size:21px;font-weight:400;line-height:26px}
.quick p{font-size:11.5px;line-height:13.5px;font-weight:600;margin:4px 0 0 3px}
.quick .field{margin-top:6px;height:31px;background:#fff;border:1px solid #ddd;font-size:11.5px;color:#aaa;font-style:italic;padding:7px 8px}

/* breadcrumb */
.crumb{left:108px;top:298px;width:654px;height:42px;background:linear-gradient(#2f7dbf,#1f64a1);color:#fff;font-size:13px;display:flex;align-items:center;padding-left:21px}
.crumb a{text-decoration:underline}
.view-toggle{position:absolute;right:0;top:0;height:42px;display:flex}
.view-toggle span{width:40px;height:42px;display:flex;align-items:center;justify-content:center}
.view-toggle span.on{background:#1a4f80}

/* search */
.search{left:770px;top:301px;width:197px;height:45px;background:#4a4a4a;padding:7px}
.search .field{width:148px;height:31px;background:#fff;font-size:11.5px;font-style:italic;color:#aaa;padding:7px 19px}
.search svg{position:absolute;right:9px;top:11px}

/* listing */
.pager{left:108px;width:654px;height:30px;border-top:1px solid #e4e4e4;border-bottom:1px solid #e4e4e4;display:flex;align-items:center;padding:0 6px;font-size:12.5px;color:#555;background:var(--page)}
.pager .num{color:var(--orange);text-decoration:underline}
.pager .pages{margin-left:auto}
.pager .loading{position:absolute;left:313px;font-size:9.5px;color:#aaa}

.grid{left:112px;top:393px;width:650px;display:grid;grid-template-columns:repeat(4,160px);column-gap:3.3px;row-gap:0}
.card{position:relative;width:160px;height:174px;background:#fff;border:1px solid #d8d8d8}
.card.partial{height:82px;overflow:hidden;border-bottom:0}
.card .head{height:29px;background:var(--card-head);color:#fff;font-size:13px;font-weight:600;padding-left:13px;line-height:29px}
.card .fav{position:absolute;right:6px;top:6px;width:17px;height:17px;background:var(--orange);display:flex;align-items:center;justify-content:center}
.card .pic{position:absolute;left:26px;top:38px;width:108px;height:88px;border-radius:3px}
.pic.monitor{background:linear-gradient(#3a3a3a,#1f1f1f);border:4px solid #222;box-shadow:inset 0 0 0 3px #f4f4f4}
.pic.laptop{background:linear-gradient(#333,#111 70%,#555)}
.pic.phones{left:46px;width:68px;border-radius:30px 30px 12px 12px;background:linear-gradient(#e8e8e8,#999)}
.card .foot{position:absolute;left:0;right:0;bottom:0;height:36px;background:var(--card-foot);display:flex;align-items:center;padding:0 6px 0 8px;font-size:12.5px;color:var(--blue-dark)}
.details{margin-left:auto;width:77px;height:23px;background:linear-gradient(#3a82c2,#246aa6);border-radius:2px;color:#fff;font-size:12.5px;display:flex;align-items:center;justify-content:center;gap:7px}
.dot{width:9px;height:9px;border-radius:50%;background:#fff;display:flex;align-items:center;justify-content:center}
.ribbon{position:absolute;left:-4px;top:96px;height:29px;padding:0 17px 0 10px;background:var(--red);color:#fff;font-size:12px;font-weight:600;line-height:29px;clip-path:polygon(0 0,100% 0,88% 50%,100% 100%,0 100%)}
.grid-fade{left:108px;top:775px;width:656px;height:52px;background:linear-gradient(rgba(247,247,247,0),var(--page) 90%)}

/* sidebar */
.tab{top:352px;height:40px;color:#fff;font-size:16px;display:flex;align-items:center;justify-content:center}
.tab.cat{left:770px;width:113px;background:var(--orange)}
.tab.filt{left:886px;width:81px;background:linear-gradient(#2f7dbf,#1f64a1)}
.catpanel{left:770px;top:392px;width:197px;height:388px;border:2px solid var(--orange);background:#535353}
.cat-head{height:38px;display:flex;align-items:center;padding:0 12px 0 12px;color:#fff;font-size:16px;background:#494949;border-bottom:1px solid #3a3a3a}
.cat-head .arr{margin-left:auto}
.sublist{list-style:none;padding:8px 0 10px 24px;height:224px;background:#5a5a5a}
.sublist li{color:#fff;font-size:12.5px;line-height:25.8px}
.side-btn{left:770px;width:197px;height:43px;background:linear-gradient(#3b86c6,#2066a3);color:#fff;font-size:18px;padding-left:15px;display:flex;align-items:center}
.more{left:767px;top:884px;width:202px;height:31px;background:var(--red);border-radius:3px 3px 0 0;color:#fff;font-size:13px;font-weight:600;display:flex;align-items:center;padding-left:39px}
.more .caret-w{margin-left:auto;margin-right:11px}

/* footer */
.footer{left:0;top:915px;width:1092px;height:236px;background:var(--footer)}
.footbar{left:0;top:1151px;width:1092px;height:49px;background:var(--footer-bottom);color:#fff;font-size:11px}
.footbar p{position:absolute;left:789px;top:20px}
.fcol h4{color:#fff;font-size:13px;font-weight:700}
.fcol p,.fcol li{color:#eee;font-size:12px;line-height:17.5px}
.qlinks{list-style:none;margin-top:19px;width:190px}
.qlinks li{padding-left:10px;line-height:25.8px;border-bottom:1px solid #3c3c3c}
.qlinks li:last-child{border:0}
.email{margin-top:14px;width:186px;height:30px;background:#fff;display:flex;align-items:center;font-style:italic;font-size:12.5px;color:#666;padding-left:10px}
.email .go{margin-left:auto;width:27px;height:30px;background:var(--orange);display:flex;align-items:center;justify-content:center}
.cards{display:grid;grid-template-columns:repeat(4,33px);gap:5px 4px;margin-top:12px}
.cards span{height:19px;border-radius:2px;background:#e9e9e9}
.cards span:nth-child(odd){background:#d5dde8}
.follow{display:flex;gap:4px;margin-top:4px}
.follow span{width:24px;height:24px;border-radius:3px}
</style>
</head>
<body>

<!-- top bar -->
<div class="abs topbar"></div>
<div class="abs country"><span class="flag"></span>United Kingdom<span class="caret"><span class="caret-w" style="border-top-color:#777"></span></span></div>
<span class="abs social-top" style="left:483px"></span>
<span class="abs social-top" style="left:528px"></span>
<span class="abs social-top" style="left:571px"></span>
<div class="abs welcome"><span class="hello">Welcome, Peter Varn</span><span class="links">My account &nbsp;|&nbsp; sign out &nbsp;|&nbsp; My Basket</span></div>

<!-- header -->
<div class="abs header"></div>
<div class="abs logo"><span class="mark"></span><span class="name">B.K. Pronto<br>Shop</span></div>
<div class="abs divider"></div>
<div class="abs tagline">Tag line <span>goes here</span></div>
<div class="abs help">
  <h2>We're Here to Help!</h2>
  <p><b>LCL:</b> 212 555 0147<br><b>TF:</b> 888 555 0192</p>
</div>
<div class="abs phone-btn">
  <svg width="18" height="18" viewBox="0 0 24 24"><path fill="#fff" d="M6.6 10.8a15 15 0 0 0 6.6 6.6l2.2-2.2c.3-.3.7-.4 1-.2 1.1.4 2.3.6 3.6.6.6 0 1 .4 1 1V20c0 .6-.4 1-1 1A17 17 0 0 1 3 4c0-.6.4-1 1-1h3.5c.6 0 1 .4 1 1 0 1.3.2 2.5.6 3.6.1.3 0 .7-.2 1z"/></svg>
</div>
<div class="abs livehelp"><div class="t1">Live Help</div><div class="t2">Talk to an advisor</div></div>

<!-- navigation -->
<nav class="abs nav">
  <a class="abs nav-item active" style="left:111px;width:110px">Hardware <span class="caret-w"></span></a>
  <a class="abs nav-item" style="left:222px;width:104px">Software <span class="caret-w"></span></a>
  <a class="abs nav-item" style="left:327px;width:130px">IT Resources <span class="caret-w"></span></a>
  <a class="abs nav-item" style="left:458px;width:121px">Technology <span class="caret-w"></span></a>
  <div class="abs cart">
    <span class="icon"><svg width="26" height="20" viewBox="0 0 26 20"><path d="M1 2h4l3 11h13l3-8H7" fill="none" stroke="#fff" stroke-width="2.2"/><circle cx="10" cy="17" r="2" fill="#fff"/><circle cx="19" cy="17" r="2" fill="#fff"/></svg></span>
    <span class="sum">0 items &nbsp;: &nbsp;£0.00</span>
  </div>
</nav>

<!-- dark band -->
<div class="abs band"></div>

<!-- special offers -->
<div class="abs offers"></div>
<div class="abs offer-strip">
  <div class="mini" style="left:0"><div class="head">Product name</div><div class="pic" role="img" aria-label="Monitor product photo"></div><div class="foot">£300.00<span class="plus"><svg width="10" height="10"><circle cx="5" cy="5" r="5" fill="#fff"/><path d="M5 2v6M2 5h6" stroke="#3d3d3d" stroke-width="1.6"/></svg></span></div></div>
  <div class="mini" style="left:115px"><div class="head">Product name</div><div class="pic" role="img" aria-label="Monitor product photo"></div><div class="foot">£300.00<span class="plus"><svg width="10" height="10"><circle cx="5" cy="5" r="5" fill="#fff"/><path d="M5 2v6M2 5h6" stroke="#3d3d3d" stroke-width="1.6"/></svg></span></div></div>
  <div class="mini" style="left:229px"><div class="head">Product name</div><div class="pic" role="img" aria-label="Monitor product photo"></div><div class="foot">£300.00<span class="plus"><svg width="10" height="10"><circle cx="5" cy="5" r="5" fill="#fff"/><path d="M5 2v6M2 5h6" stroke="#3d3d3d" stroke-width="1.6"/></svg></span></div></div>
  <div class="mini" style="left:343px"><div class="head">Product name</div><div class="pic" role="img" aria-label="Monitor product photo"></div><div class="foot">£300.00<span class="plus"><svg width="10" height="10"><circle cx="5" cy="5" r="5" fill="#fff"/><path d="M5 2v6M2 5h6" stroke="#3d3d3d" stroke-width="1.6"/></svg></span></div></div>
  <div class="mini" style="left:458px"><div class="head">Product name</div><div class="pic" role="img" aria-label="Monitor product photo"></div><div class="foot">£300.00<span class="plus"><svg width="10" height="10"><circle cx="5" cy="5" r="5" fill="#fff"/><path d="M5 2v6M2 5h6" stroke="#3d3d3d" stroke-width="1.6"/></svg></span></div></div>
</div>
<div class="abs offer-tag">
  <svg width="108" height="114" viewBox="0 0 108 114"><polygon points="0,0 84,0 108,57 84,114 0,114" fill="#ea4140"/></svg>
  <div class="label">Special<br>Offers</div>
</div>
<div class="abs offer-arrows"><span>‹</span><span>›</span></div>

<!-- quick shop -->
<div class="abs quick">
  <h3>Quick shop</h3>
  <p>SKU number or Model number to &nbsp;add the product to your basket</p>
  <div class="field">e.g. model number</div>
</div>

<!-- breadcrumb -->
<div class="abs crumb">
  <a>Home</a>&nbsp;- &nbsp;Harware
  <div class="view-toggle">
    <span><svg width="28" height="26"><g fill="#174b79"><rect x="0" y="0" width="8" height="7"/><rect x="10" y="0" width="8" height="7"/><rect x="20" y="0" width="8" height="7"/><rect x="0" y="9" width="8" height="8"/><rect x="10" y="9" width="8" height="8"/><rect x="20" y="9" width="8" height="8"/><rect x="0" y="19" width="8" height="7"/><rect x="10" y="19" width="8" height="7"/><rect x="20" y="19" width="8" height="7"/></g></svg></span>
    <span class="on"><svg width="28" height="26"><g fill="#6f9fc9"><rect x="0" y="0" width="6" height="5"/><rect x="7" y="0" width="6" height="5"/><rect x="14" y="0" width="6" height="5"/><rect x="21" y="0" width="6" height="5"/><rect x="0" y="7" width="6" height="5"/><rect x="7" y="7" width="6" height="5"/><rect x="14" y="7" width="6" height="5"/><rect x="21" y="7" width="6" height="5"/><rect x="0" y="14" width="6" height="5"/><rect x="7" y="14" width="6" height="5"/><rect x="14" y="14" width="6" height="5"/><rect x="21" y="14" width="6" height="5"/><rect x="0" y="21" width="6" height="5"/><rect x="7" y="21" width="6" height="5"/><rect x="14" y="21" width="6" height="5"/><rect x="21" y="21" width="6" height="5"/></g></svg></span>
  </div>
</div>

<!-- search -->
<div class="abs search">
  <div class="field">Product search</div>
  <svg width="24" height="24" viewBox="0 0 24 24"><circle cx="14" cy="9" r="7" fill="none" stroke="#fff" stroke-width="2.4"/><path d="M9 14l-7 7" stroke="#fff" stroke-width="3"/></svg>
</div>

<!-- listing -->
<div class="abs pager" style="top:350px">View&nbsp;<span class="num">80</span>&nbsp;products per page<span class="pages">1 &nbsp;<span class="num">2</span>&nbsp; Next</span></div>

<div class="abs grid">
  <div class="card"><div class="head">Product name</div><span class="fav"><svg width="11" height="11" viewBox="0 0 24 24"><path fill="#fff" d="M12 2l3 7 7 .6-5.3 4.6 1.6 7.2L12 17.6 5.7 21.4l1.6-7.2L2 9.6 9 9z"/></svg></span><div class="pic monitor" role="img" aria-label="Flat screen monitor"></div><span class="ribbon">Best seller</span><div class="foot">£300.00<span class="details">Details <span class="dot"><svg width="5" height="5"><path d="M1 0l3 2.5L1 5z" fill="#246aa6"/></svg></span></span></div></div>
  <div class="card"><div class="head">Product name</div><span class="fav"><svg width="11" height="11" viewBox="0 0 24 24"><path fill="#fff" d="M12 2l3 7 7 .6-5.3 4.6 1.6 7.2L12 17.6 5.7 21.4l1.6-7.2L2 9.6 9 9z"/></svg></span><div class="pic laptop" role="img" aria-label="Laptop computer"></div><div class="foot">£2990.00<span class="details">Details <span class="dot"><svg width="5" height="5"><path d="M1 0l3 2.5L1 5z" fill="#246aa6"/></svg></span></span></div></div>
  <div class="card"><div class="head">Product name</div><span class="fav"><svg width="11" height="11" viewBox="0 0 24 24"><path fill="#fff" d="M12 2l3 7 7 .6-5.3 4.6 1.6 7.2L12 17.6 5.7 21.4l1.6-7.2L2 9.6 9 9z"/></svg></span><div class="pic phones" role="img" aria-label="Over-ear headphones"></div><div class="foot">£70.00<span class="details">Details <span class="dot"><svg width="5" height="5"><path d="M1 0l3 2.5L1 5z" fill="#246aa6"/></svg></span></span></div></div>
  <div class="card"><div class="head">Product name</div><span class="fav"><svg width="11" height="11" viewBox="0 0 24 24"><path fill="#fff" d="M12 2l3 7 7 .6-5.3 4.6 1.6 7.2L12 17.6 5.7 21.4l1.6-7.2L2 9.6 9 9z"/></svg></span><div class="pic monitor" role="img" aria-label="Flat screen monitor"></div><div class="foot">£390.99<span class="details">Details <span class="dot"><svg width="5" height="5"><path d="M1 0l3 2.5L1 5z" fill="#246aa6"/></svg></span></span></div></div>

  <div class="card"><div class="head">Product name</div><span class="fav"><svg width="11" height="11" viewBox="0 0 24 24"><path fill="#fff" d="M12 2l3 7 7 .6-5.3 4.6 1.6 7.2L12 17.6 5.7 21.4l1.6-7.2L2 9.6 9 9z"/></svg></span><div class="pic monitor" role="img" aria-label="Flat screen monitor"></div><div class="foot">£300.00<span class="details">Details <span class="dot"><svg width="5" height="5"><path d="M1 0l3 2.5L1 5z" fill="#246aa6"/></svg></span></span></div></div>
  <div class="card"><div class="head">Product name</div><span class="fav"><svg width="11" height="11" viewBox="0 0 24 24"><path fill="#fff" d="M12 2l3 7 7 .6-5.3 4.6 1.6 7.2L12 17.6 5.7 21.4l1.6-7.2L2 9.6 9 9z"/></svg></span><div class="pic laptop" role="img" aria-label="Laptop computer"></div><div class="foot">£2990.00<span class="details">Details <span class="dot"><svg width="5" height="5"><path d="M1 0l3 2.5L1 5z" fill="#246aa6"/></svg></span></span></div></div>
  <div class="card"><div class="head">Product name</div><span class="fav"><svg width="11" height="11" viewBox="0 0 24 24"><path fill="#fff" d="M12 2l3 7 7 .6-5.3 4.6 1.6 7.2L12 17.6 5.7 21.4l1.6-7.2L2 9.6 9 9z"/></svg></span><div class="pic phones" role="img" aria-label="Over-ear headphones"></div><span class="ribbon">Best seller</span><div class="foot">£70.00<span class="details">Details <span class="dot"><svg width="5" height="5"><path d="M1 0l3 2.5L1 5z" fill="#246aa6"/></svg></span></span></div></div>
  <div class="card"><div class="head">Product name</div><span class="fav"><svg width="11" height="11" viewBox="0 0 24 24"><path fill="#fff" d="M12 2l3 7 7 .6-5.3 4.6 1.6 7.2L12 17.6 5.7 21.4l1.6-7.2L2 9.6 9 9z"/></svg></span><div class="pic monitor" role="img" aria-label="Flat screen monitor"></div><div class="foot">£390.99<span class="details">Details <span class="dot"><svg width="5" height="5"><path d="M1 0l3 2.5L1 5z" fill="#246aa6"/></svg></span></span></div></div>

  <div class="card partial"><div class="head">Product name</div><span class="fav"><svg width="11" height="11" viewBox="0 0 24 24"><path fill="#fff" d="M12 2l3 7 7 .6-5.3 4.6 1.6 7.2L12 17.6 5.7 21.4l1.6-7.2L2 9.6 9 9z"/></svg></span><div class="pic monitor" role="img" aria-label="Flat screen monitor"></div></div>
  <div class="card partial"><div class="head">Product name</div><span class="fav"><svg width="11" height="11" viewBox="0 0 24 24"><path fill="#fff" d="M12 2l3 7 7 .6-5.3 4.6 1.6 7.2L12 17.6 5.7 21.4l1.6-7.2L2 9.6 9 9z"/></svg></span><div class="pic laptop" role="img" aria-label="Laptop computer"></div></div>
  <div class="card partial"><div class="head">Product name</div><span class="fav"><svg width="11" height="11" viewBox="0 0 24 24"><path fill="#fff" d="M12 2l3 7 7 .6-5.3 4.6 1.6 7.2L12 17.6 5.7 21.4l1.6-7.2L2 9.6 9 9z"/></svg></span><div class="pic phones" role="img" aria-label="Over-ear headphones"></div></div>
  <div class="card partial"><div class="head">Product name</div><span class="fav"><svg width="11" height="11" viewBox="0 0 24 24"><path fill="#fff" d="M12 2l3 7 7 .6-5.3 4.6 1.6 7.2L12 17.6 5.7 21.4l1.6-7.2L2 9.6 9 9z"/></svg></span><div class="pic monitor" role="img" aria-label="Flat screen monitor"></div></div>
</div>
<div class="abs grid-fade"></div>

<div class="abs pager" style="top:856px">View&nbsp;<span class="num">80</span>&nbsp;products per page<span class="loading">loading more products</span><span class="pages">1 &nbsp;<span class="num">2</span>&nbsp; Next</span></div>

<!-- sidebar -->
<div class="abs tab cat">Categories</div>
<div class="abs tab filt">Filters</div>
<div class="abs catpanel">
  <div class="cat-head" style="background:linear-gradient(#2f7dbf,#1f64a1)">Hardware<span class="arr"><svg width="9" height="6"><path d="M0 6l4.5-5L9 6z" fill="#fff"/></svg></span></div>
  <ul class="sublist">
    <li>Desktops</li><li>Laptops &amp; Notebooks</li><li>Components</li><li>Tablets</li><li>Software</li><li>Phones &amp; PDAs</li><li>Cameras</li><li>MP3 Players</li>
  </ul>
  <div class="cat-head">Software<span class="arr caret-w"></span></div>
  <div class="cat-head">IT Resources<span class="arr caret-w"></span></div>
  <div class="cat-head" style="border:0">Technology<span class="arr caret-w"></span></div>
</div>
<a class="abs side-btn" style="top:786px">My Account</a>
<a class="abs side-btn" style="top:834px">Contact us</a>
<a class="abs more">More information<span class="caret-w"></span></a>

<!-- footer -->
<footer class="abs footer">
  <div class="abs fcol" style="left:120px;top:21px">
    <h4>Quick links</h4>
    <ul class="qlinks">
      <li>Shop</li><li>Latest offers</li><li>Shopping basket</li><li>Press office / corporate site</li><li>Terms and conditions</li><li>Sitemap</li>
    </ul>
  </div>
  <div class="abs fcol" style="left:343px;top:21px;width:190px">
    <h4>Email Sign up</h4>
    <p style="margin-top:20px">Keep up-to-date with all of our latest products and special offers</p>
    <p style="margin-top:9px">Sign up to our newsletter</p>
    <div class="email" style="margin-left:-2px">Email address<span class="go"><svg width="6" height="8"><path d="M0 0l6 4-6 4z" fill="#fff"/></svg></span></div>
  </div>
  <div class="abs fcol" style="left:554px;top:23px">
    <h4>Payment options</h4>
    <p style="margin-top:20px">We accept all of the payments below</p>
    <div class="cards" role="img" aria-label="Accepted payment methods"><span></span><span></span><span></span><span></span><span></span><span></span><span></span><span></span></div>
  </div>
  <div class="abs fcol" style="left:773px;top:23px;width:195px">
    <h4>Contact details</h4>
    <p style="margin-top:20px;font-size:11px">Lorem ipsum dolor sit amet, consectetur adipiscing elit. Proin aliquet, enim quis sagittis rutrum, purus metus posuere nibh, sit</p>
    <p style="margin-top:15px;font-size:11px">info@bkprontosystems.com</p>
    <p style="margin-top:13px;font-size:16px;color:#fff">Stay in touch</p>
    <div class="follow" style="margin-left:-4px"><span style="background:#3b5b9c"></span><span style="background:#6cc7ec"></span><span style="background:#f28a1e"></span></div>
  </div>
</footer>
<div class="abs footbar"><p>Copyright 2013 · All rights reserved</p></div>

</body>
</html>
```